Square Business Cards for Our Restaurant / Event Venue

We need square business cards designed for the management team of our event venue and restaurant. On one side of the card should be the the Harbor Lantern 7 logo and URL www.harborlantern7.example. On the other side should be the Ember Logo and URL www.emberhall7.example. All employee details should be on the side with Ember logo. There will be a total of 5 cards to be created with the design.

Clara Bennquist
clara@harborlantern7.example

main 555.418.3072
direct 555.730.2946

4831 West Orchard Lane SE
Washington, DC 90417

Industry/Entity Type

Business

```html
<!DOCTYPE html>
<html lang="en">
<head>
<meta charset="utf-8">
<title>Harbor Lantern 7 – Square Business Cards</title>
<link rel="stylesheet" href="https://fonts.googleapis.com/css2?family=Montserrat:wght@400;500;600&display=swap">
<style>
  :root {
    --backdrop: #e8e5e1;
    --venue-red: #b81f25;
    --card-black: #000000;
    --paper-white: #ffffff;
    --text-font: "Montserrat", Arial, sans-serif;
  }
  * { margin: 0; padding: 0; box-sizing: border-box; }
  html, body {
    width: 1200px;
    height: 900px;
    overflow: hidden;
    background: var(--backdrop);
    font-family: var(--text-font);
  }
  .canvas { position: relative; width: 1200px; height: 900px; }

  .card {
    position: absolute;
    width: 378px;
    height: 378px;
    border-radius: 16px;
    overflow: hidden;
  }

  /* Venue side */
  .card--venue { left: 710px; top: 34px; background: var(--venue-red); }
  .venue-badge {
    position: absolute;
    left: 83px; top: 61px;
    width: 210px; height: 210px;
    border-radius: 50%;
    background: var(--paper-white);
    display: flex; align-items: center; justify-content: center;
    text-align: center;
  }
  .venue-name {
    color: var(--venue-red);
    font-weight: 400;
    font-size: 27px;
    line-height: 1.2;
  }
  .venue-url {
    position: absolute;
    left: 0; right: 0; top: 300px;
    text-align: center;
    color: var(--paper-white);
    font-weight: 600;
    font-size: 19.5px;
    letter-spacing: 0.2px;
    white-space: nowrap;
  }

  /* Staff side */
  .card--staff { left: 117px; top: 480px; background: var(--card-black); color: var(--paper-white); }
  .staff-contact {
    position: absolute;
    left: 18px; top: 354px;
    width: 336px;
    transform-origin: 0 0;
    transform: rotate(-90deg);
    white-space: nowrap;
  }
  .staff-name { font-size: 21px; line-height: 26px; font-weight: 400; letter-spacing: 0.5px; }
  .staff-email { margin-top: 4px; font-size: 16.5px; line-height: 22px; font-weight: 400; letter-spacing: 0.2px; }

  .hall-info {
    position: absolute;
    left: 82px; right: 6px; top: 0;
    text-align: center;
  }
  .hall-name {
    margin-top: 36px;
    height: 110px;
    display: flex; align-items: center; justify-content: center;
    font-size: 64px;
    font-weight: 500;
    letter-spacing: 1px;
  }
  .hall-url { margin-top: 16px; font-size: 19px; font-weight: 600; letter-spacing: 0.2px; white-space: nowrap; }
  .contact-icon { display: block; margin: 12px auto 2px; }
  .contact-line { font-size: 16.5px; line-height: 24px; font-weight: 400; white-space: nowrap; }
</style>
</head>
<body>
<main class="canvas">

  <section class="card card--venue" aria-label="Venue side of card">
    <div class="venue-badge">
      <p class="venue-name">Harbor<br>Lantern 7</p>
    </div>
    <p class="venue-url">www.harborlantern7.example</p>
  </section>

  <section class="card card--staff" aria-label="Staff side of card">
    <div class="staff-contact">
      <p class="staff-name">Clara Bennquist</p>
      <p class="staff-email">clara@harborlantern7.example</p>
    </div>

    <div class="hall-info">
      <p class="hall-name">Ember</p>
      <p class="hall-url">www.emberhall7.example</p>

      <svg class="contact-icon" width="24" height="20" viewBox="0 0 24 20" aria-label="Phone">
        <path d="M2 7 C2 2 22 2 22 7 L17 8 L16 5 C13 4 11 4 8 5 L7 8 Z" fill="#fff"/>
        <path d="M6 9 L18 9 L21 18 L3 18 Z" fill="#fff"/>
        <circle cx="12" cy="13.5" r="2.6" fill="#000"/>
      </svg>
      <p class="contact-line">main 555.418.3072</p>
      <p class="contact-line">direct 555.730.2946</p>

      <svg class="contact-icon" width="28" height="26" viewBox="0 0 28 26" aria-label="Address">
        <path d="M14 1 L27 13 L23 13 L23 25 L5 25 L5 13 L1 13 Z" fill="#fff"/>
        <rect x="11.5" y="16" width="5" height="9" fill="#000"/>
      </svg>
      <p class="contact-line">4831 West Orchard Lane SE</p>
      <p class="contact-line">Washington, DC 90417</p>
    </div>
  </section>

</main>
</body>
</html>
```